Harbor Mortgage Relief

Please help us give our website a remake or a FACELIFT. It is not very good but it says what we need it to say. But the design is terrible.
I would like our new design font and logo to be used as the theme.

I also want more photos on the site.

I also want consistency with the pages so they look clean.

We want the professionals to do this, let's see what you got!

Thank you!
Updates

Project Deadline Extended
Reason: I can understand you want to be paid. So I will commit to the fee but I want you to have time to make a KICK ASS website for me dudes! Thanks

HI!  Just wanted to say thanks for your time on these.  A lot are great.  However the firefighters have nothing to do with Foreclosure.  We are saving peoples homes from the bank taking them and selling them.   I LOVE the house photos and the families on the website.  That is the direction we like.  THanks.

THANK U ALL FOR THE WORK!   I like a few ending in the numbers: 147  733  693  536  620  478  727  508     I will go over them and choose one soon.  Thank you.   You will be paid shortly. 

Requirements
Must have
• Bright, Upbeat photos. Color scheme should be in order. We like icons on the bottom. not just text.

```html
<!DOCTYPE html>
<html lang="en">
<head>
<meta charset="utf-8">
<title>Harbor Mortgage Relief</title>
<link href="https://fonts.googleapis.com/css2?family=Montserrat:wght@400;500;600;700&family=Open+Sans:wght@400;600&display=swap" rel="stylesheet">
<style>
:root{
  --red:#e3262c;
  --red-dark:#b8161b;
  --ink:#4a4a4a;
  --heading:#555;
  --header-bg:#efece7;
  --sky:#8fcbeb;
  --sky-deep:#5fb0dd;
  --testimonial-bg:#8fc9ea;
  --testimonial-title:#1d3f63;
  --footer-bg:#2e2e30;
  --footer-text:#f2f2f2;
  --footer-muted:#9a9a9a;
  --social:#3b8fd0;
}
*{margin:0;padding:0;box-sizing:border-box}
html,body{width:1172px;height:1200px;overflow:hidden;background:#fff}
body{font-family:"Open Sans",Arial,sans-serif;color:var(--ink);position:relative}

.site-header{position:absolute;left:0;top:0;width:1172px;height:152px;background:var(--header-bg);border-bottom:6px solid #e2ded8}
.brand{position:absolute;left:138px;top:22px;display:flex;align-items:center;gap:12px}
.brand-mark{width:86px;height:86px;border-radius:50%;background:var(--red)}
.brand-name{font-family:"Montserrat",sans-serif;font-weight:700;font-size:25px;line-height:26px;color:var(--red);text-transform:uppercase;width:200px}
.spanish{position:absolute;left:652px;top:28px;font-family:"Montserrat",sans-serif;font-weight:600;font-size:16px;color:#222;letter-spacing:.3px}
.call{position:absolute;left:836px;top:22px;display:flex;gap:10px;align-items:flex-start}
.call-label{font-family:"Montserrat",sans-serif;font-size:14px;font-weight:500;color:#222;line-height:14px;margin-top:2px}
.call-number{font-family:"Montserrat",sans-serif;font-size:25px;font-weight:500;color:var(--red);line-height:28px}
.main-nav{position:absolute;left:456px;top:77px;width:587px;height:33px;background:linear-gradient(var(--red),var(--red-dark));border-radius:3px;display:flex}
.main-nav a{font-family:"Montserrat",sans-serif;font-size:14px;color:#fff;text-decoration:none;line-height:33px;text-align:center;border-right:1px solid #9e1216}
.main-nav a:last-child{border-right:0}

.hero{position:absolute;left:138px;top:129px;width:905px;height:326px;border-radius:6px;background:linear-gradient(180deg,#a8d9f3 0%,#7cc3ea 45%,#d9eef9 52%,#86c8ec 56%,#7fc2e8 100%);overflow:hidden}
.hero-house{position:absolute;left:470px;top:30px;width:360px;height:290px;background:linear-gradient(160deg,#5a6070 0%,#e7b948 40%,#d9a73a 100%);border-radius:4px;opacity:.85}

.welcome{position:absolute;left:138px;top:480px;width:650px}
.welcome h1{font-family:"Montserrat",sans-serif;font-weight:700;font-size:20.5px;color:var(--heading);letter-spacing:.2px;margin-bottom:17px}
.welcome h1 .accent{color:var(--red)}
.welcome p{font-size:14px;line-height:21px;margin-bottom:21px;color:var(--ink)}

.testimonials{position:absolute;left:815px;top:477px;width:228px;height:511px;background:var(--testimonial-bg);border-radius:6px;padding:12px 12px 0 12px}
.testimonials h2{font-family:"Montserrat",sans-serif;font-weight:600;font-size:19.5px;color:var(--testimonial-title);margin-bottom:8px}
.quote{position:relative;padding-left:30px;margin-bottom:18px}
.quote::before{content:"\201C";position:absolute;left:0;top:-6px;font-family:Georgia,serif;font-size:50px;line-height:50px;color:#fff}
.quote p{font-size:12.6px;line-height:16.5px;color:#fff}
.quote cite{display:block;font-style:normal;font-family:"Montserrat",sans-serif;font-size:12px;color:var(--testimonial-title);margin-top:6px}

.site-footer{position:absolute;left:0;top:1004px;width:1172px;height:196px;background:var(--footer-bg);border-top:4px solid var(--red)}
.footer-col{position:absolute;color:var(--footer-text);font-family:"Montserrat",sans-serif}
.email-col{left:138px;top:24px;width:270px}
.email-icon{display:block;margin:0 0 6px 92px}
.email-col a{font-size:13px;color:var(--footer-text);text-decoration:none;text-transform:uppercase}
.mailing{left:440px;top:34px}
.col-title{font-size:13px;text-transform:uppercase;margin-bottom:8px;display:block}
.mail-input{width:180px;height:24px;border-radius:4px;background:#9a9a9a;color:#e8e8e8;font-family:"Open Sans",sans-serif;font-size:11.5px;line-height:24px;padding-left:9px;margin-bottom:9px}
.join-btn{width:54px;height:25px;border-radius:3px;background:linear-gradient(#f4f4f4,#bdbdbd);color:#333;font-size:14px;text-align:center;line-height:25px;font-family:"Open Sans",sans-serif}
.follow{left:667px;top:34px}
.social{display:flex;gap:9px}
.social span{width:30px;height:30px;border-radius:3px;background:var(--social)}
.address{left:815px;top:34px;font-size:13.5px;line-height:21px}
.footer-rule{position:absolute;left:138px;top:147px;width:905px;height:1px;background:#444}
.copyright{position:absolute;left:0;top:165px;width:1172px;text-align:center;font-size:11.5px;color:var(--footer-muted);font-family:"Montserrat",sans-serif}
</style>
</head>
<body>

<header class="site-header">
  <div class="brand">
    <span class="brand-mark"></span>
    <span class="brand-name">Harbor Mortgage Relief</span>
  </div>
  <div class="spanish">HABLAMOS ESPANOL</div>
  <div class="call">
    <svg width="32" height="32" viewBox="0 0 32 32" aria-hidden="true">
      <rect width="32" height="32" rx="5" fill="#e3262c"/>
      <path d="M11 7c1 0 2 3 2.5 4.5.3 1-1.5 2-1.2 3 .8 2 2.6 4 4.4 5 1 .5 2-1.4 3-1 1.5.5 4.5 1.5 4.5 2.5 0 2-2 4-4 4C15 25 7 17 7 11c0-2 2-4 4-4z" fill="#fff"/>
    </svg>
    <div>
      <div class="call-label">CALL TOLL FREE NOW</div>
      <div class="call-number">877-555-0142</div>
    </div>
  </div>
  <nav class="main-nav">
    <a href="#" style="width:85px">HOME</a>
    <a href="#" style="width:105px">ABOUT US</a>
    <a href="#" style="width:102px">SERVICES</a>
    <a href="#" style="width:123px">CONTACT US</a>
    <a href="#" style="width:172px">OWNER OPTIONS</a>
  </nav>
</header>

<section class="hero" role="img" aria-label="Photo of a yellow house sinking into clear blue water with a for-sale sign on the roof">
  <div class="hero-house"></div>
</section>

<main class="welcome">
  <h1>WELCOME TO <span class="accent">HARBOR</span> MORTGAGE <span class="accent">RELIEF</span></h1>
  <p>HARBOR MORTGAGE RELIEF specializes in assisting homeowners who are in FORECLOSURE, by offering solid alternatives to losing your home in a Trustee Sale.&nbsp; Having your home foreclosed on can damage your credit for up to 7 years.&nbsp; Most foreclosures end with the home owner being evicted from their home, leaving them with no money, no place to live and without ample time to safely remove their possessions from their home.&nbsp; There is no need to have this happen to you.&nbsp; No matter what part of foreclosure process you are in, WE CAN HELP!</p>
  <p>If you have received a Notice of Default (NOD) or Notice of Trustee Sale (NTS), you have options. Contact us today to speak to one of our licensed specialist, and let us help you put this situation behind you.</p>
  <p>We speak to hundreds of homeowners every day, we understand how frustrating this can be.&nbsp; Don't live in fear of what is to come.&nbsp; You have other options, please call or email us today and we will immediately put our specialist to work finding you a solution.</p>
  <p>Don't try to handle this frustrating situation by yourself.&nbsp; HARBOR MORTGAGE RELIEF is a team of knowledgeable real estate professionals, we can offer you a better solution during this tough time.</p>
  <p>HARBOR MORTGAGE RELIEF has been assisting families in foreclosure for years.&nbsp; Our skill and integrity has earned us a reputation for fast, professional, courteous and thorough solutions.&nbsp; With over 50 years of real estate knowledge and experience HARBOR MORTGAGE RELIEF is ready to assist you.</p>
</main>

<aside class="testimonials">
  <h2>Testimonals</h2>
  <blockquote class="quote">
    <p>I'd like to express my gratitude to you and your company and I have to add, for all of the trustworthy and reliable service that you bring to the public.&nbsp; Your company helped put me back together, you in particular are wesome! Thank you again Theo.</p>
    <cite>Rosa</cite>
  </blockquote>
  <blockquote class="quote">
    <p>Harbor Mortgage Relief has been an absolute life saver for me and my family. Their services have changed everything.&nbsp; Instead of my house going into foreclosure and losing everything I own, I now have a chance to start over and the money to do it with!&nbsp; They've been fast, friendly and efficient.&nbsp; I would recommend their services to anyone facing foreclosure.</p>
    <cite>Dana K.</cite>
  </blockquote>
</aside>

<footer class="site-footer">
  <div class="footer-col email-col">
    <svg class="email-icon" width="76" height="58" viewBox="0 0 76 58" aria-hidden="true">
      <rect x="4" y="8" width="68" height="44" rx="4" fill="#3aa6dc"/>
      <path d="M4 12l34 24 34-24" fill="none" stroke="#1f6fa3" stroke-width="3"/>
    </svg>
    <a href="#">info@harbormortgagerelief.com</a>
  </div>
  <div class="footer-col mailing">
    <span class="col-title">Join our mailing list</span>
    <div class="mail-input">Your e-mail address</div>
    <div class="join-btn">Join</div>
  </div>
  <div class="footer-col follow">
    <span class="col-title">Follow us</span>
    <div class="social"><span></span><span></span><span></span></div>
  </div>
  <address class="footer-col address" style="font-style:normal">
    HARBOR MORTGAGE RELIEF<br>
    218 Harbor Street Suite 300<br>
    Bayview, CA 90210<br>
    877-555-0142
  </address>
  <div class="footer-rule"></div>
  <div class="copyright">© 2012. HARBORMORTGAGERELIEF.COM. All rights reserved.&nbsp; Reserved | Privacy Policy</div>
</footer>

</body>
</html>
```